Presentation card Venture KELO - Tech Incubator from Perú

We need a Design to promote the incubator of technology Startups.
We are in Perú, we work with a string tech filter and develop enterprenurship competencies in the Startup team.
The card is to facilitators and staff memebers of VentureKELO.
We want a clear, modern, tech and agile Design.

We work to help New enterprises of technology here in Perú, we expect the candidates have a big competencies to Research and develop technological products.

We work using methodologies from QRB, Folmestry, Brakewell and Harrowgate univeesities. Our book base is the disciplina of enterpreneur.

We work events all year using diferent formats: Brightforge, Vorne price, OPRA Model Competition you can use these logros in your Design.

Set the name, role, email, cell phone number, address.

Example:
// Contact info section
Tobías Quiroveda
Swift Modeling Hub Manager
tobias.quiroveda@kelo-example.pe
(511) 999 000 417

// Address info section
VentureKELO
Technology-based business incubator
Av. Los Cedrales 884, Valdora
Lima - Perú
web: venture-kelo-example.org.pe
email: venture@kelo-example.pe
phone number: (511) 3926508 ext. 4418

// (optional)Lema section
Making happy using technology

// Social network section
facebook: venturekelooficial

Target Market(s)

Enterprenurship, CTO, Investors, Companies interested on open innovation services

Industry/Entity Type

Information Technology

Contact Information for Business Card

Name, Role, Email, Cell phone number

Colors

Designer to choose colors to be used in the design.

Requirements
Must have
• Logo forms and colors
Nice to have
• I add pictures of the leaders of incubator
Should not have
• No vertical designs

```html
<!DOCTYPE html>
<html lang="en">
<head>
<meta charset="utf-8">
<title>Venture KELO – Business Card</title>
<link href="https://fonts.googleapis.com/css2?family=Montserrat:wght@400;700;800&display=swap" rel="stylesheet">
<style>
  :root {
    --crimson: #c0395a;
    --ink: #2b2b2b;
    --paper: #ffffff;
    --backdrop: #e4e2df;
    --photo-dark: #4a3f3a;
    --photo-mid: #7a6458;
    --photo-light: #a48a78;
  }
  * { box-sizing: border-box; margin: 0; padding: 0; }
  html, body {
    width: 1051px; height: 1200px; overflow: hidden;
    background: var(--backdrop);
    font-family: "Montserrat", sans-serif;
    color: var(--ink);
  }
  .card {
    position: absolute; left: 75px; width: 900px; height: 514px;
    box-shadow: 0 6px 18px rgba(0,0,0,.25);
    overflow: hidden;
  }
  .card--front { top: 62px; background: var(--paper); }
  .card--back { top: 620px; }

  .brand-mark {
    position: absolute; left: 95px; top: 222px;
    font-weight: 800; font-size: 46px; line-height: 1;
    color: var(--ink); letter-spacing: -0.5px;
  }
  .info-block { position: absolute; left: 450px; padding-left: 29px; border-left: 2px solid var(--crimson); }
  .info-block--company { top: 52px; }
  .info-block--person { top: 330px; }
  .info-block h2 {
    font-weight: 700; font-size: 27px; color: var(--crimson);
    letter-spacing: 0.5px; line-height: 1.05; margin-bottom: 2px;
  }
  .info-block p { font-size: 20px; line-height: 26px; letter-spacing: 0.3px; }
  .contact-list { position: absolute; left: 479px; list-style: none; }
  .contact-list--company { top: 212px; }
  .contact-list--person { top: 487px; transform: translateY(-100%); }
  .contact-list li { display: flex; align-items: center; font-size: 20px; line-height: 26px; letter-spacing: 0.3px; }
  .contact-list svg { width: 15px; height: 15px; margin-right: 16px; fill: var(--crimson); flex: none; }

  .photo {
    position: absolute; inset: 0;
    background: linear-gradient(160deg, var(--photo-light) 0%, var(--photo-mid) 45%, var(--photo-dark) 100%);
  }
  .back-mark {
    position: absolute; left: 0; right: 0; top: 218px; text-align: center;
    font-weight: 800; font-size: 52px; color: #fff; letter-spacing: -0.5px;
  }
  .achievements {
    position: absolute; left: 85px; right: 40px; top: 455px;
    display: flex; gap: 42px; list-style: none;
    color: #fff; font-weight: 700; font-size: 20px; letter-spacing: 0.6px; text-transform: uppercase;
  }
  .achievements li::before {
    content: ""; display: inline-block; width: 10px; height: 10px; border-radius: 50%;
    background: #fff; margin-right: 8px; vertical-align: 2px;
  }
</style>
</head>
<body>
  <section class="card card--front">
    <div class="brand-mark">Venture KELO</div>

    <div class="info-block info-block--company">
      <h2>VENTUREKELO</h2>
      <p>Technology-based business incubator</p>
      <p>Av. Los Cedrales 884, Valdora</p>
      <p>Lima - Perú</p>
    </div>
    <ul class="contact-list contact-list--company">
      <li><svg viewBox="0 0 16 16"><circle cx="8" cy="8" r="7" fill="none" stroke="#c0395a" stroke-width="1.6"/><path d="M1 8h14M8 1c-4 4-4 10 0 14M8 1c4 4 4 10 0 14" fill="none" stroke="#c0395a" stroke-width="1.3"/></svg>venture-kelo-example.org.pe</li>
      <li><svg viewBox="0 0 16 16"><rect x="1" y="3" width="14" height="10"/><path d="M1 3l7 6 7-6" fill="none" stroke="#fff" stroke-width="1.2"/></svg>venture@kelo-example.pe</li>
      <li><svg viewBox="0 0 16 16"><path d="M3 1l3 0 1 4-2 1.5c1 2 2.5 3.5 4.5 4.5L11 9l4 1v3c0 1-1 2-2 2C7 15 1 9 1 3c0-1 1-2 2-2z"/></svg>(511) 3926508 ext. 4418</li>
    </ul>

    <div class="info-block info-block--person">
      <h2>TOBÍAS QUIROVEDA</h2>
      <p>Swift Modeling Hub Manager</p>
    </div>
    <ul class="contact-list contact-list--person">
      <li><svg viewBox="0 0 16 16"><rect x="1" y="3" width="14" height="10"/><path d="M1 3l7 6 7-6" fill="none" stroke="#fff" stroke-width="1.2"/></svg>tobias.quiroveda@kelo-example.pe</li>
      <li><svg viewBox="0 0 16 16"><path d="M3 1l3 0 1 4-2 1.5c1 2 2.5 3.5 4.5 4.5L11 9l4 1v3c0 1-1 2-2 2C7 15 1 9 1 3c0-1 1-2 2-2z"/></svg>(511) 999 000 417</li>
    </ul>
  </section>

  <section class="card card--back">
    <div class="photo" role="img" aria-label="Group photo of the incubator team and participants standing together in a workspace"></div>
    <div class="back-mark">Venture KELO</div>
    <ul class="achievements">
      <li>Brightforge</li>
      <li>Vorne price</li>
      <li>OPRA Model Competition</li>
    </ul>
  </section>
</body>
</html>
```